Floor Inspections and Consulting

We provide inspections and consulting services on various floor coverings, e.g. carpet, hardwood, etc. We also do expert witness work for attorneys due to floor covering failures. We current have a logo, just need it incorporated into a new design. I have examples of cards I have found on the internet that capture my attention and make a statement. I have included our original business card, which in my opinion is terrible, but it does have our logo on it.

```html
<!DOCTYPE html>
<html lang="en">
<head>
<meta charset="utf-8">
<title>Northgrade Floors – Business Card</title>
<link href="https://fonts.googleapis.com/css2?family=Open+Sans:wght@400;600;700&display=swap" rel="stylesheet">
<style>
  :root {
    --stage: #5f6b73;
    --card-white: #ffffff;
    --ink: #1b1f24;
    --ink-soft: #2c3238;
    --blue: #0a6fd6;
    --blue-deep: #0a3f9e;
    --blue-light: #1aa3ea;
    --navy-dark: #0b1620;
    --slate: #8d99a2;
    --rule: #e3e7ea;
  }
  * { box-sizing: border-box; margin: 0; padding: 0; }
  html, body {
    width: 1200px; height: 900px; overflow: hidden;
    background: var(--stage);
    font-family: "Open Sans", Arial, sans-serif;
  }
  .canvas { position: relative; width: 1200px; height: 900px; }
  .card {
    position: absolute; left: 285px; width: 630px; height: 360px;
    overflow: hidden; border-radius: 4px;
    box-shadow: 0 14px 30px rgba(0,0,0,.35);
  }
  .card--front { top: 60px; background: var(--card-white); }
  .card--back { top: 480px; background: var(--navy-dark); }
  .card-art { position: absolute; inset: 0; width: 100%; height: 100%; }

  .brand-mark {
    position: absolute; display: flex; flex-direction: column;
    align-items: center; justify-content: center; gap: 10px; text-align: center;
    color: var(--card-white); font-weight: 700; letter-spacing: .12em;
  }
  .brand-mark__dot {
    width: 16px; height: 16px; border-radius: 50%; background: var(--card-white);
  }
  .card--front .brand-mark { left: 95px; top: 95px; width: 190px; height: 170px; font-size: 17px; line-height: 1.25; }
  .card--back .brand-mark { left: 215px; top: 80px; width: 200px; height: 120px; font-size: 22px; line-height: 1.2; }

  .person-name {
    position: absolute; left: 325px; top: 82px;
    font-size: 27px; font-weight: 700; color: var(--ink); letter-spacing: .01em;
  }
  .contact-list { position: absolute; left: 330px; top: 178px; list-style: none; }
  .contact-list li {
    display: flex; align-items: center; gap: 12px;
    font-size: 15px; color: var(--ink-soft); margin-bottom: 11px;
  }
  .contact-list svg { width: 15px; height: 15px; flex: none; }

  .tagline {
    position: absolute; left: 0; right: 0; top: 222px; text-align: center;
    color: #e9eef2; font-size: 21px; line-height: 1.4; font-weight: 400;
  }
</style>
</head>
<body>
<main class="canvas">

  <section class="card card--front" aria-label="Card front">
    <svg class="card-art" viewBox="0 0 630 360" aria-hidden="true">
      <defs>
        <linearGradient id="slate-fade" x1="0" y1="0" x2="1" y2="1">
          <stop offset="0" stop-color="#8d99a2"/>
          <stop offset=".55" stop-color="#1c2a36"/>
          <stop offset="1" stop-color="#07111a"/>
        </linearGradient>
        <linearGradient id="blue-tile" x1="0" y1="0" x2="1" y2="1">
          <stop offset="0" stop-color="#1aa3ea"/>
          <stop offset=".6" stop-color="#0a6fd6"/>
          <stop offset="1" stop-color="#0a3f9e"/>
        </linearGradient>
        <linearGradient id="blue-corner" x1="0" y1="0" x2="1" y2="1">
          <stop offset="0" stop-color="#1aa3ea"/>
          <stop offset="1" stop-color="#0a4fb8"/>
        </linearGradient>
      </defs>
      <!-- dark backing panel -->
      <rect x="-40" y="-10" width="290" height="300" rx="28" fill="#d9dee2"/>
      <rect x="-40" y="-20" width="280" height="300" rx="28" fill="url(#slate-fade)"/>
      <!-- blue tile -->
      <rect x="96" y="86" width="200" height="198" rx="22" fill="#dfe4e8"/>
      <rect x="90" y="80" width="200" height="198" rx="22" fill="url(#blue-tile)"/>
      <!-- corner accents -->
      <path d="M560 0 H630 V58 H584 Q566 58 560 40 Z" fill="url(#blue-corner)"/>
      <path d="M0 300 H100 Q112 300 108 314 L96 360 H0 Z" fill="url(#blue-corner)"/>
    </svg>
    <div class="brand-mark">
      <span class="brand-mark__dot"></span>
      <span>NORTHGRADE<br>FLOORS</span>
    </div>
    <h1 class="person-name">DANA WHITCOMBE</h1>
    <ul class="contact-list">
      <li>
        <svg viewBox="0 0 16 16" aria-hidden="true"><circle cx="8" cy="8" r="7" fill="none" stroke="#0a6fd6" stroke-width="1.4"/><path d="M5.2 4.8l1.4-.4.8 1.8-.9.7a5 5 0 0 0 2.4 2.4l.7-.9 1.8.8-.4 1.4c-3 .2-6-2.8-5.8-5.8z" fill="#0a6fd6"/></svg>
        555-012-4477
      </li>
      <li>
        <svg viewBox="0 0 16 16" aria-hidden="true"><rect x="1.5" y="3.5" width="13" height="9" rx="1" fill="none" stroke="#0a6fd6" stroke-width="1.4"/><path d="M2 4l6 5 6-5" fill="none" stroke="#0a6fd6" stroke-width="1.4"/></svg>
        dana@northgradefloors.com
      </li>
      <li>
        <svg viewBox="0 0 16 16" aria-hidden="true"><circle cx="8" cy="8" r="6.5" fill="none" stroke="#0a6fd6" stroke-width="1.4"/><ellipse cx="8" cy="8" rx="2.8" ry="6.5" fill="none" stroke="#0a6fd6" stroke-width="1.2"/><path d="M1.5 8h13" stroke="#0a6fd6" stroke-width="1.2"/></svg>
        northgradefloors.com
      </li>
    </ul>
  </section>

  <section class="card card--back" aria-label="Card back">
    <svg class="card-art" viewBox="0 0 630 360" aria-hidden="true">
      <defs>
        <radialGradient id="back-glow" cx=".5" cy=".38" r=".62">
          <stop offset="0" stop-color="#8d99a2"/>
          <stop offset=".5" stop-color="#2c3b47"/>
          <stop offset="1" stop-color="#07111a"/>
        </radialGradient>
        <linearGradient id="blue-corner-b" x1="0" y1="0" x2="1" y2="1">
          <stop offset="0" stop-color="#1aa3ea"/>
          <stop offset="1" stop-color="#0a4fb8"/>
        </linearGradient>
      </defs>
      <rect width="630" height="360" fill="url(#back-glow)"/>
      <path d="M560 0 H630 V58 H584 Q566 58 560 40 Z" fill="url(#blue-corner-b)"/>
      <path d="M0 300 H100 Q112 300 108 314 L96 360 H0 Z" fill="url(#blue-corner-b)"/>
    </svg>
    <div class="brand-mark">
      <span class="brand-mark__dot"></span>
      <span>NORTHGRADE<br>FLOORS</span>
    </div>
    <p class="tagline">Certified Floor Covering<br>Inspections &amp; Consulting</p>
  </section>

</main>
</body>
</html>
```